need eczema bath soak label/bag

need you to recreate this please. ai file. recreate this exact image please. ...if you want a big tip, create some different styles.

Colors
0054AA
0677BA
7BADD7
CADEEF
E8F1F8

```html
<!DOCTYPE html>
<html lang="en">
<head>
<meta charset="UTF-8">
<title>The Ocean Healed My A Bag — Bath Soak Pouch Label</title>
<link href="https://fonts.googleapis.com/css2?family=Montserrat:wght@600;700;800&display=swap" rel="stylesheet">
<style>
  :root {
    --backdrop: #d9d8d6;
    --ink: #163b41;
    --cream: #eef0e4;
    --foam: #f4f7f6;
    --sea-light: #cfe7e4;
    --sea: #8ccfcc;
    --sea-deep: #6fbcb8;
    --shore: #e6dccb;
    --sand-light: #d8b884;
    --sand: #c9a46c;
    --sand-deep: #bc955e;
  }
  * { margin: 0; padding: 0; box-sizing: border-box; }
  html, body {
    width: 1200px;
    height: 1115px;
    overflow: hidden;
    background: var(--backdrop);
  }
  .canvas {
    position: relative;
    width: 1200px;
    height: 1115px;
  }
  .label {
    position: absolute;
    left: 248px;
    top: 60px;
    width: 704px;
    height: 1030px;
    overflow: hidden;
    font-family: "Montserrat", sans-serif;
    color: var(--ink);
    text-align: center;
  }
  .label__scene {
    position: absolute;
    inset: 0;
    background: linear-gradient(
      to bottom,
      var(--cream) 0%,
      var(--cream) 18%,
      var(--foam) 26%,
      var(--foam) 34%,
      var(--sea-light) 40%,
      var(--sea) 47%,
      var(--sea-deep) 55%,
      var(--sea) 61%,
      var(--sea-light) 65%,
      var(--shore) 68%,
      var(--sand-light) 72%,
      var(--sand) 85%,
      var(--sand-deep) 100%
    );
  }
  .label__content {
    position: absolute;
    inset: 0;
  }
  .headline {
    position: absolute;
    top: 262px;
    left: 0;
    right: 0;
    font-weight: 700;
    line-height: 1;
  }
  .headline__lead {
    display: block;
    font-size: 27px;
    letter-spacing: 0.28em;
    margin-bottom: 28px;
    padding-left: 0.28em;
  }
  .headline__line {
    display: block;
    font-size: 60px;
    margin-bottom: 18px;
  }
  .headline__line--wide {
    letter-spacing: 0.12em;
    padding-left: 0.12em;
  }
  .blurb {
    position: absolute;
    top: 562px;
    left: 0;
    right: 0;
    font-size: 12.5px;
    font-weight: 700;
    line-height: 25px;
    letter-spacing: 0.02em;
  }
  .tagline {
    position: absolute;
    top: 650px;
    left: 0;
    right: 0;
    font-size: 20px;
    font-weight: 700;
    letter-spacing: 0.08em;
    padding-right: 40px;
  }
  .brand {
    position: absolute;
    top: 860px;
    left: 0;
    right: 0;
    display: flex;
    flex-direction: column;
    align-items: center;
    gap: 18px;
  }
  .brand__mark {
    width: 46px;
    height: 46px;
    background: var(--ink);
  }
  .brand__name {
    font-size: 18px;
    font-weight: 700;
    letter-spacing: 0.12em;
    color: var(--ink);
  }
</style>
</head>
<body>
  <main class="canvas">
    <section class="label">
      <div class="label__scene" role="img" aria-label="Watercolour beach scene: pale sky fading into turquoise sea foam over golden sand"></div>
      <div class="label__content">
        <h1 class="headline">
          <span class="headline__lead">THE</span>
          <span class="headline__line headline__line--wide">OCEAN</span>
          <span class="headline__line">HEALED</span>
          <span class="headline__line">MY A BAG</span>
        </h1>
        <p class="blurb">
          Lorem ipsumLorem ipsumLorem<br>
          ipsumLorem ipsumLorem ipsumLorem<br>
          ipsumLorem ipsumLorem ipsum
        </p>
        <p class="tagline">OCEAN | IN A BA</p>
        <div class="brand">
          <span class="brand__mark"></span>
          <span class="brand__name">TIDEWELL</span>
        </div>
      </div>
    </section>
  </main>
</body>
</html>
```